Need webpage for TUTORING COMPANY

Hello,
Our tutoring company Quillbrook Tutorials is launching a new program named 'Daylight Walk-Home Program'.
We would like a website created to showcase our new program.
Our current company page is: www.quillbrook.org
The new program webpage can have a link on the current company page that takes you to the new program webpage. We are open to ideas in regards to this. I would like the new program page to have the following:
-student online registration
-a way for parents to schedule their calendar days for the program
-a way for parents to pay (pricing is $45 a day or $745 per month)
The web content will be similar to this: http://pebblecoveclubhouse.com/
I personally did not like their website and I prefer a modern, sleek, structured, eye catchy design.
We need the website fairly quickly.
Thank you,
Varsha Menon
P.S: I am attaching the flyer & brochure for the new program.
School
After School Program by QuillBrook Tutoriails

```html
<!DOCTYPE html>
<html lang="en">
<head>
<meta charset="utf-8">
<title>Daylight Walk-Home Program</title>
<link href="https://fonts.googleapis.com/css2?family=Open+Sans:wght@400;600;700&family=Oswald:wght@500&display=swap" rel="stylesheet">
<style>
:root{
  --forest:#1d3b2a;
  --forest-deep:#142b1e;
  --orange:#f0871e;
  --orange-dark:#d46f0c;
  --page:#e9ece8;
  --paper:#ffffff;
  --ink:#2b2b2b;
  --muted:#6b6b6b;
  --mint:#cfe3c2;
  --sky:#eef5f8;
  --bus:#f4c430;
}
*{box-sizing:border-box;margin:0;padding:0}
html,body{width:878px;height:1200px;overflow:hidden}
body{background:var(--page);font-family:"Open Sans",Arial,sans-serif;color:var(--ink);font-size:8px;line-height:1.5}
.site{width:878px;height:1200px;position:relative;display:flex;flex-direction:column}
.masthead{height:44px;background:var(--forest);position:relative;flex:none}
.brand{position:absolute;left:76px;top:13px;display:flex;align-items:center;gap:6px;color:#fff;font-weight:700;font-size:12px;letter-spacing:.5px}
.brand-dot{width:14px;height:14px;border-radius:50%;background:var(--orange)}
.title-tab{position:absolute;left:50%;transform:translateX(-50%);top:0;background:var(--orange);color:#fff;font-family:"Oswald",Arial,sans-serif;font-size:24px;font-weight:500;line-height:1.3;padding:6px 28px;border-radius:0 0 6px 6px;white-space:nowrap}
.tagline{text-align:center;padding-top:14px;height:58px;background:var(--sky);flex:none}
.tagline h2{font-size:15px;font-weight:700;color:var(--forest);line-height:1.3}
.tagline p{font-size:9px;color:var(--muted)}
.hero{height:226px;flex:none;background:var(--sky);padding:0 150px}
.hero-art{height:100%;border-radius:10px 10px 0 0;background:linear-gradient(180deg,#f8d65a 0%,var(--bus) 100%)}
.nav{height:28px;flex:none;background:var(--forest);display:flex;justify-content:center;gap:38px;align-items:center;color:#fff;font-size:9px;font-weight:600}
.wrap{width:732px;margin:0 auto;background:var(--paper);flex:1;display:flex;flex-direction:column}
.actions{background:var(--forest-deep);padding:14px;display:flex;gap:14px;height:168px;flex:none}
.action{flex:1;border:2px solid var(--orange);padding:14px;color:#dfe6df;display:flex;gap:12px}
.action-icon{width:44px;height:44px;border-radius:50%;background:var(--orange);flex:none;display:flex;align-items:center;justify-content:center}
.action h3{color:var(--orange);font-size:14px;line-height:1.3;margin-bottom:4px}
.action p{font-size:7.5px}
.btn{display:inline-block;margin-top:10px;background:var(--orange);color:#fff;font-size:8px;font-weight:600;padding:4px 12px;border-radius:3px}
.section{padding:14px 18px 0}
.section h2{font-size:12px;font-weight:700;color:var(--forest);border-bottom:1px solid #dcdcdc;padding-bottom:4px;margin-bottom:8px}
.section p{color:var(--muted);font-size:7.5px;margin-bottom:6px}
.cards{display:flex;gap:12px;padding-top:14px}
.card{flex:1;border:1px solid var(--orange);text-align:center;padding:22px 10px 10px;position:relative;height:128px}
.card-num{position:absolute;top:-12px;left:50%;transform:translateX(-50%);width:24px;height:24px;border-radius:50%;background:var(--orange);color:#fff;font-weight:700;font-size:12px;line-height:24px}
.card h3{color:var(--orange-dark);font-size:10px;margin-bottom:4px}
.card p{font-size:7.5px;color:var(--muted)}
.schedule{display:flex;gap:16px}
.schedule-text{flex:1}
.calendar{width:170px;border:1px solid #ccc;font-size:7px;flex:none}
.cal-head{background:var(--orange);color:#fff;display:flex;justify-content:space-between;padding:3px 6px;font-weight:700}
.calendar table{width:100%;border-collapse:collapse;text-align:center}
.calendar th{background:#f3f3f3;font-weight:600;padding:2px 0}
.calendar td{padding:2px 0;border-top:1px solid #eee}
.calendar td.today{background:var(--orange);color:#fff}
.contact{margin-top:auto;background:var(--mint);height:50px;flex:none;display:flex;align-items:center;justify-content:space-around;font-size:10px;font-weight:600;color:var(--forest)}
.contact span{display:flex;align-items:center;gap:8px}
.ic{width:24px;height:24px;border-radius:50%;background:var(--orange);display:flex;align-items:center;justify-content:center}
.footer{height:24px;flex:none;background:var(--forest);color:#cfd8cf;font-size:7.5px;display:flex;align-items:center;justify-content:space-between;padding:0 73px}
.socials{display:flex;gap:6px}
.socials i{width:9px;height:9px;border-radius:50%;background:#9db59d;display:block}
</style>
</head>
<body>
<div class="site">
  <header class="masthead">
    <div class="brand"><span class="brand-dot"></span>QUILLBROOK</div>
    <h1 class="title-tab">Daylight Walk-Home Program</h1>
  </header>
  <div class="tagline">
    <h2>Perfect Solution For Busy Parents</h2>
    <p>Now Enrolling Grades K-8</p>
  </div>
  <div class="hero"><div class="hero-art" role="img" aria-label="Illustration of a yellow school bus carrying children, parked on grass"></div></div>
  <nav class="nav"><span>Home</span><span>About Our Program</span><span>Principle</span><span>Calendar</span><span>Contact Us</span></nav>

  <main class="wrap">
    <section class="actions">
      <div class="action">
        <div class="action-icon"><svg width="22" height="22" viewBox="0 0 24 24" fill="#fff"><circle cx="12" cy="8" r="4"/><path d="M4 21c0-4.4 3.6-7 8-7s8 2.6 8 7z"/></svg></div>
        <div>
          <h3>Student Registration</h3>
          <p>Sign up your child online in minutes. Choose grade, school and pickup days, add emergency contacts and any notes for our staff. Spots fill quickly each term, so register early to secure a place.</p>
          <span class="btn">Register Now</span>
        </div>
      </div>
      <div class="action">
        <div class="action-icon"><svg width="22" height="22" viewBox="0 0 24 24" fill="#fff"><rect x="3" y="6" width="18" height="12" rx="2"/><rect x="3" y="9" width="18" height="2" fill="#f0871e"/></svg></div>
        <div>
          <h3>Pay for Your Kids</h3>
          <p>Pay securely online at $45 per day or $745 per month. Receipts are emailed right away and you can review past payments at any time from your parent account with no extra fees.</p>
          <span class="btn">Pay Now</span>
        </div>
      </div>
    </section>

    <section class="section">
      <h2>Welcome to Daylight Walk-Home Program</h2>
      <p>Our program gives working families peace of mind. Trained staff meet students at dismissal, walk them safely to our center and guide them through a structured afternoon of homework, snacks, play and learning until parents arrive for pickup at the end of the day.</p>
      <p>We keep groups small and attentive, share daily updates with parents and partner closely with local schools. Every afternoon balances focused study with creative activities so children head home relaxed, confident and ready for tomorrow's lessons.</p>
    </section>

    <section class="section">
      <h2>Our Program</h2>
      <div class="cards">
        <div class="card"><span class="card-num">1</span><h3>After School Pick-Up</h3><p>Staff meet students at school and walk them safely to our center each afternoon.</p></div>
        <div class="card"><span class="card-num">2</span><h3>Homeroom</h3><p>Quiet study time with tutors on hand to help finish daily homework.</p></div>
        <div class="card"><span class="card-num">3</span><h3>Enrichment Exercises</h3><p>Fun math and reading challenges that build skills beyond the classroom.</p></div>
        <div class="card"><span class="card-num">4</span><h3>Extra Curriculars</h3><p>Art, games and outdoor play to round out a healthy, happy afternoon.</p></div>
      </div>
    </section>

    <section class="section">
      <h2>Schedule Your Calendar</h2>
      <div class="schedule">
        <div class="schedule-text">
          <p>Pick the days that suit your family. Select single days or a full month, and change your plan whenever your schedule shifts, right from this page.</p>
          <p>Booked days appear highlighted on the calendar. You will get a reminder the evening before each session so nothing slips through.</p>
          <p>Need a late pickup or a one-off change? Send a note with your booking and our team will confirm within one business day.</p>
        </div>
        <div class="calendar">
          <div class="cal-head"><span>&lsaquo;</span><span>September</span><span>&rsaquo;</span></div>
          <table>
            <tr><th>Su</th><th>Mo</th><th>Tu</th><th>We</th><th>Th</th><th>Fr</th><th>Sa</th></tr>
            <tr><td></td><td>1</td><td>2</td><td>3</td><td>4</td><td>5</td><td>6</td></tr>
            <tr><td>7</td><td>8</td><td>9</td><td>10</td><td>11</td><td>12</td><td>13</td></tr>
            <tr><td>14</td><td>15</td><td class="today">16</td><td>17</td><td>18</td><td>19</td><td>20</td></tr>
            <tr><td>21</td><td>22</td><td>23</td><td>24</td><td>25</td><td>26</td><td>27</td></tr>
            <tr><td>28</td><td>29</td><td>30</td><td></td><td></td><td></td><td></td></tr>
          </table>
        </div>
      </div>
    </section>

    <section class="contact">
      <span><i class="ic"><svg width="12" height="12" viewBox="0 0 24 24" fill="#fff"><path d="M12 2a7 7 0 0 0-7 7c0 5 7 13 7 13s7-8 7-13a7 7 0 0 0-7-7zm0 9.5A2.5 2.5 0 1 1 12 6.5a2.5 2.5 0 0 1 0 5z"/></svg></i>418 Lantern Row, Suite 90 Fairhaven, TX 75410</span>
      <span><i class="ic"><svg width="12" height="12" viewBox="0 0 24 24" fill="#fff"><path d="M6.6 10.8a15 15 0 0 0 6.6 6.6l2.2-2.2a1 1 0 0 1 1-.25 11 11 0 0 0 3.6.6 1 1 0 0 1 1 1V20a1 1 0 0 1-1 1A17 17 0 0 1 3 4a1 1 0 0 1 1-1h3.5a1 1 0 0 1 1 1c0 1.25.2 2.45.6 3.6a1 1 0 0 1-.25 1z"/></svg></i>(555)302-4186 &nbsp;(555)302-7719</span>
    </section>
  </main>

  <footer class="footer">
    <span>&copy;2024 Daylight Walk-Home Program. All Rights Reserved</span>
    <div class="socials"><i></i><i></i><i></i></div>
  </footer>
</div>
</body>
</html>
```